Book Cover Design Project

Cover design using photo provided.
Title is as follows:-

Harold Edmund Pellow

"Letters from the Quiet Orchard"

By Dennis Halloway

Just Added Picture and extended design a further 7 days

```html
<!DOCTYPE html>
<html lang="en">
<head>
<meta charset="UTF-8">
<title>Harold Edmund Pellow – Letters from the Quiet Orchard</title>
<link rel="stylesheet" href="https://fonts.googleapis.com/css2?family=Yellowtail&family=Tinos:wght@400;700&display=swap">
<style>
  :root {
    --portrait-light: #d7a66c;
    --portrait-mid: #b67a3f;
    --portrait-warm: #9c5a2c;
    --portrait-dark: #4e2b16;
    --title-white: rgba(250, 247, 243, 0.94);
    --author-black: #120c08;
  }
  html, body {
    margin: 0;
    padding: 0;
    width: 800px;
    height: 1200px;
    overflow: hidden;
    background: #ffffff;
  }
  .cover {
    position: relative;
    width: 800px;
    height: 1200px;
    overflow: hidden;
  }
  .cover-portrait {
    position: absolute;
    inset: 0;
    background:
      radial-gradient(ellipse 55% 40% at 45% 42%, rgba(232, 190, 130, 0.85), rgba(232, 190, 130, 0) 70%),
      radial-gradient(ellipse 60% 50% at 70% 30%, rgba(200, 140, 80, 0.6), rgba(200, 140, 80, 0) 70%),
      linear-gradient(180deg, var(--portrait-mid) 0%, var(--portrait-light) 35%, var(--portrait-warm) 65%, var(--portrait-dark) 100%);
  }
  .author-name {
    position: absolute;
    top: 16px;
    left: 0;
    width: 100%;
    margin: 0;
    text-align: center;
    font-family: "Tinos", "Times New Roman", serif;
    font-weight: 400;
    font-size: 30px;
    color: var(--author-black);
  }
  .book-title {
    position: absolute;
    top: 50px;
    left: 0;
    width: 100%;
    margin: 0;
    font-family: "Yellowtail", cursive;
    font-weight: 400;
    font-size: 178px;
    line-height: 150px;
    color: var(--title-white);
    text-align: center;
  }
  .book-title span {
    display: block;
  }
  .book-subtitle {
    position: absolute;
    top: 600px;
    left: 18px;
    right: 10px;
    margin: 0;
    font-family: "Tinos", "Times New Roman", serif;
    font-weight: 400;
    font-size: 110px;
    line-height: 138px;
    letter-spacing: -2px;
    color: var(--title-white);
    text-align: center;
  }
  .book-subtitle span {
    display: block;
    white-space: nowrap;
  }
</style>
</head>
<body>
  <main class="cover">
    <div class="cover-portrait" role="img" aria-label="Close-up sepia portrait photograph of the book's subject, filling the whole cover"></div>
    <p class="author-name">Dennis Halloway</p>
    <h1 class="book-title">
      <span>Harold</span>
      <span>Edmund</span>
      <span>Pellow</span>
    </h1>
    <h2 class="book-subtitle">
      <span>Letters from the</span>
      <span>Quiet Orchard</span>
    </h2>
  </main>
</body>
</html>
```